We want to design total new business card and logo for Kestrel Building Services Ltd

Our company name Kestrel Building Services Ltd. Design new logo and business card , need hi-end luxury style art for architecture and construction industry. The card should simple but stylish. Our business focus on CONNECT tradesman to construction company, help marketing construction company tender oversea projects, managing franchise in construction sector, delivery amazing services to our client, so Logo should show the CONNECTION IDEA, CONNECTING PEOPLE, LUXURY. Visit our website for more information: kestrelhub.co.nz

Low design quality

Target Market(s)

Directors or managers

Industry/Entity Type

Construction Company

Contact Information for Business Card

Name, Title, Mobile, Email, Website

Font styles to use
Serif

Colors

Designer to choose colors to be used in the design.

Requirements
Must have
• Simple and luxury, connection icon
Nice to have
• Special materials, plastic card, look through,...
• Look new ideas.

```html
<!DOCTYPE html>
<html lang="en">
<head>
<meta charset="utf-8">
<title>Kestrel Building Services – Business Card</title>
<link href="https://fonts.googleapis.com/css2?family=Open+Sans:wght@400;600;700&display=swap" rel="stylesheet">
<style>
  :root {
    --page-bg: #e9eaec;
    --brand-blue: #0aa7c9;
    --brand-blue-text: #13a6c8;
    --panel-light: #f4f5f6;
    --panel-light-edge: #e9ebec;
    --tagline: #545454;
    --white: #ffffff;
    --divider: rgba(255,255,255,0.55);
  }
  * { box-sizing: border-box; margin: 0; padding: 0; }
  html, body { width: 1200px; height: 900px; overflow: hidden; }
  body {
    background: var(--page-bg);
    font-family: "Open Sans", Arial, sans-serif;
    position: relative;
  }
  .business-card {
    position: absolute;
    left: 110px; top: 147px;
    width: 980px; height: 606px;
    background: var(--brand-blue);
    overflow: hidden;
    box-shadow: 0 10px 30px rgba(0,0,0,0.15);
  }
  .brand-panel {
    position: absolute;
    left: 0; top: 89px;
    width: 100%; height: 234px;
    background: linear-gradient(180deg, var(--panel-light) 0%, var(--panel-light-edge) 100%);
    text-align: center;
  }
  .brand-mark {
    position: absolute;
    left: 435px; top: 24px;
    width: 110px; height: 110px;
    border-radius: 50%;
    background: var(--brand-blue);
    border: 6px solid var(--white);
    z-index: 2;
  }
  .brand-name {
    position: absolute;
    left: 0; right: 0; top: 78px;
    font-size: 43px;
    font-weight: 700;
    color: var(--brand-blue-text);
    letter-spacing: 0.5px;
  }
  .brand-tagline {
    position: absolute;
    left: 0; right: 0; top: 153px;
    font-size: 27px;
    font-weight: 400;
    color: var(--tagline);
    letter-spacing: 0.5px;
  }
  .person {
    position: absolute;
    right: 524px; top: 376px;
    text-align: right;
    color: var(--white);
  }
  .person-name { font-size: 33px; font-weight: 700; line-height: 1.1; letter-spacing: 0.3px; }
  .person-title { font-size: 27px; font-weight: 400; line-height: 1.2; }
  .contact-divider {
    position: absolute;
    left: 489px; top: 350px;
    width: 2px; height: 130px;
    background: var(--divider);
  }
  .contact-list {
    position: absolute;
    left: 514px; top: 343px;
    list-style: none;
    color: var(--white);
    font-size: 27px;
    line-height: 36px;
  }
  .contact-list li { display: flex; align-items: center; }
  .contact-icon { width: 22px; height: 22px; margin-right: 14px; fill: var(--white); flex: none; }
  .company-address {
    position: absolute;
    left: 0; right: 0; top: 506px;
    text-align: center;
    color: var(--white);
    font-size: 27px;
    line-height: 35px;
    font-style: normal;
  }
</style>
</head>
<body>
  <div class="business-card">
    <div class="brand-mark" aria-hidden="true"></div>

    <section class="brand-panel">
      <h1 class="brand-name">KESTREL BUILDING SERVICES</h1>
      <p class="brand-tagline">AMAZING SERVICES AFFORDABLE PRICE</p>
    </section>

    <div class="person">
      <p class="person-name">MARCUS HALE</p>
      <p class="person-title">Managing Director</p>
    </div>

    <div class="contact-divider"></div>

    <ul class="contact-list">
      <li>
        <svg class="contact-icon" viewBox="0 0 24 24" aria-hidden="true"><path d="M3 8c0-2 4-4 9-4s9 2 9 4v2h-5V8.5c-1-.5-2.5-.8-4-.8s-3 .3-4 .8V10H3z"/><path d="M7 11h10l3 8H4z"/><circle cx="12" cy="15" r="2" fill="#0aa7c9"/></svg>
        0800 123 456
      </li>
      <li>
        <svg class="contact-icon" viewBox="0 0 24 24" aria-hidden="true"><path d="M3 8c0-2 4-4 9-4s9 2 9 4v2h-5V8.5c-1-.5-2.5-.8-4-.8s-3 .3-4 .8V10H3z"/><path d="M7 11h10l3 8H4z"/><circle cx="12" cy="15" r="2" fill="#0aa7c9"/></svg>
        021 555 0142
      </li>
      <li>
        <svg class="contact-icon" viewBox="0 0 24 24" aria-hidden="true"><rect x="3" y="6" width="18" height="12"/><path d="M3 6l9 7 9-7" fill="none" stroke="#0aa7c9" stroke-width="1.8"/></svg>
        info@kestrelhub.co.nz
      </li>
      <li>
        <svg class="contact-icon" viewBox="0 0 24 24" aria-hidden="true"><circle cx="12" cy="12" r="9"/><path d="M3 12h18M12 3c3 3 3 15 0 18M12 3c-3 3-3 15 0 18" fill="none" stroke="#0aa7c9" stroke-width="1.4"/></svg>
        www.kestrelhub.co.nz
      </li>
    </ul>

    <address class="company-address">
      KESTREL BUILDING SERVICES LTD<br>
      18 Totara Lane, Riverside, Westhaven 4012, New Zealand
    </address>
  </div>
</body>
</html>
```